BIX Promotional flyer for students

We're looking for an 8.5" x 11" flyer that will be distributed to schools. Please see language to include in attached files.

Target Market(s)

The parents and teachers of high school students

Industry/Entity Type

Mental health

Other font styles liked:
• Monserrat and Roboto Slab

Requirements
Must have
• See attached pdf for language to be included on the flyer. Please use the color palette from our website: www.bixzone.tv. Please include some imagery of students. Please ensure the
Nice to have
• Feel free to use any of the graphics provided. See our website for our brand look & feel: www.bixzone.tv

```html
<!DOCTYPE html>
<html lang="en">
<head>
<meta charset="utf-8">
<title>Fundraise with BIX – Flyer</title>
<link rel="stylesheet" href="https://fonts.googleapis.com/css2?family=Montserrat:wght@400;500;600;700&family=Roboto+Slab:wght@700;800&display=swap">
<style>
  :root {
    --ink: #111111;
    --brand-blue: #1a7dc4;
    --brand-orange: #f07a2e;
    --mist: #edf2f6;
    --steel: #6a9ab5;
    --paper: #ffffff;
    --canvas: #ffffff;
    --photo-warm: #b89a78;
    --photo-cool: #8c9fae;
    --photo-mixed: #a08f84;
  }
  * { margin: 0; padding: 0; box-sizing: border-box; }
  html, body { width: 1200px; height: 2318px; overflow: hidden; background: var(--canvas); }
  body { position: relative; font-family: "Montserrat", sans-serif; color: var(--ink); }

  .flyer {
    position: absolute; left: 196px; top: 150px; width: 820px; height: 1062px;
    background: var(--paper); overflow: hidden;
    box-shadow: 0 12px 24px rgba(0,0,0,0.22);
  }
  .flyer-decor { position: absolute; inset: 0; }

  .headline-row { position: absolute; left: 68px; top: 122px; display: flex; align-items: center; }
  .headline-row .fundraise {
    font-family: "Roboto Slab", serif; font-weight: 800; font-size: 49px; letter-spacing: 0.5px;
  }
  .headline-row .with { font-weight: 700; font-size: 19px; margin: 6px 14px 0 16px; letter-spacing: 1px; }
  .brand-mark { display: flex; align-items: center; gap: 6px; }
  .brand-mark .dot { width: 18px; height: 18px; border-radius: 50%; background: var(--brand-orange); }
  .brand-mark .name { font-weight: 700; font-size: 34px; color: var(--brand-orange); }

  .tagline {
    position: absolute; left: 67px; top: 198px; font-weight: 500; font-size: 20px; letter-spacing: 0.4px;
    white-space: nowrap;
  }
  .tagline .sep { color: var(--brand-orange); margin: 0 18px; }

  .photo { position: absolute; border: 0 solid var(--paper); }
  .photo.group   { left: 69px;  top: 263px; width: 298px; height: 342px; background: linear-gradient(160deg, #7c8a4e, var(--photo-warm) 55%, #6f8fa8); }
  .photo.student { left: 69px;  top: 573px; width: 132px; height: 177px; background: linear-gradient(170deg, #d8d8d8, var(--photo-cool)); border-width: 0 4px 4px 0; }
  .photo.class   { left: 211px; top: 615px; width: 156px; height: 145px; background: linear-gradient(160deg, #c9b8a4, var(--photo-mixed)); }
  .photo.hallway { left: 69px;  top: 758px; width: 189px; height: 124px; background: linear-gradient(150deg, #d6b48e, #3f4650); }
  .photo.study   { left: 265px; top: 770px; width: 102px; height: 112px; background: linear-gradient(160deg, #c8b492, #8d8a6d); }

  .accent-bar { position: absolute; left: 412px; top: 355px; width: 174px; height: 14px; background: var(--brand-orange); }

  .title {
    position: absolute; left: 411px; top: 392px;
    font-family: "Roboto Slab", serif; font-weight: 800; font-size: 55px; line-height: 53px;
    color: var(--brand-blue); text-transform: uppercase;
  }
  .body-copy {
    position: absolute; left: 417px; top: 672px; width: 360px;
    font-size: 19px; line-height: 28.3px; font-weight: 400;
  }
  .body-copy b { font-weight: 600; }

  .web { position: absolute; left: 417px; top: 910px; display: flex; align-items: center; gap: 10px; font-weight: 700; font-size: 21px; }
</style>
</head>
<body>
  <main class="flyer">
    <svg class="flyer-decor" width="820" height="1062" viewBox="0 0 820 1062" aria-hidden="true">
      <circle cx="60" cy="140" r="389" fill="var(--mist)"/>
      <circle cx="820" cy="1062" r="170" fill="var(--steel)"/>
    </svg>

    <div class="headline-row">
      <span class="fundraise">FUNDRAISE</span>
      <span class="with">WITH</span>
      <span class="brand-mark"><span class="dot"></span><span class="name">BIX</span></span>
    </div>

    <p class="tagline">50% OF ALL PROCEEDS<span class="sep">•</span>GO BACK TO YOUR SCHOOL</p>

    <div class="photo group" role="img" aria-label="Three smiling high school girls holding notebooks outdoors"></div>
    <div class="photo student" role="img" aria-label="Male student holding books in a library"></div>
    <div class="photo class" role="img" aria-label="Students sitting together in a classroom"></div>
    <div class="photo hallway" role="img" aria-label="Two students talking in a school hallway"></div>
    <div class="photo study" role="img" aria-label="Student writing at a desk"></div>

    <div class="accent-bar"></div>
    <h1 class="title">Support<br>the mental<br>health<br>of your<br>students</h1>

    <p class="body-copy">BIX is a <b>simple</b> and <b>effective way</b> to improve <b>mental health.</b> Your students will learn valuable coping skills and techniques from expert clinicians who analyze real cases and share their insights and advice.</p>

    <div class="web">
      <svg width="26" height="26" viewBox="0 0 26 26" aria-hidden="true">
        <g fill="none" stroke="var(--brand-blue)" stroke-width="2.2">
          <circle cx="13" cy="13" r="11"/>
          <ellipse cx="13" cy="13" rx="5" ry="11"/>
          <line x1="2" y1="13" x2="24" y2="13"/>
          <path d="M4 7.5h18M4 18.5h18"/>
        </g>
      </svg>
      <span>bixzone.tv</span>
    </div>
  </main>
</body>
</html>
```